CPA Firm Stationary & Business Cards
Whitfield & Partners CPAs PSC
CPA Firm Stationary & Business Cards - Financial Services
Creative Brief
Professional
Martin L. Dowse, CPA
Shareholder
4815 Tillamore Ave. Suite 1 Marlow Falls, OR 97019
mdowse@wpfcpa.net
www.wpfcpa.net
We are a CPA (Certified Public Accountant) firm, in business since 1924. In addition to Business Cards, I would also like to see designs for Letterheads and Envelopes.
Your choice. At a minimum, it should include the "W" logo.In addition to Business Cards, I would also like to see designs for Letterheads and Envelopes.

```html
<!DOCTYPE html>
<html lang="en">
<head>
<meta charset="utf-8">
<title>Whitfield &amp; Partners CPAs PSC — Business Card</title>
<link href="https://fonts.googleapis.com/css2?family=PT+Sans:wght@400;700&display=swap" rel="stylesheet">
<style>
  :root{
    --bg:#ececec;
    --paper:#ffffff;
    --blue-deep:#1746b8;
    --blue:#2a66d6;
    --blue-light:#4fa3ec;
    --ink:#4a4f57;
    --muted:#8a9099;
    --tab:#c9ccd1;
  }
  *{margin:0;padding:0;box-sizing:border-box}
  html,body{width:1200px;height:1009px;overflow:hidden}
  body{background:var(--bg);font-family:"PT Sans",Arial,sans-serif;position:relative}
  .card{position:absolute;left:210px;width:780px;height:446px;border-radius:26px;overflow:hidden;box-shadow:0 6px 18px rgba(0,0,0,.12)}
  .card--back{top:40px;background:linear-gradient(135deg,var(--blue-light) 0%,var(--blue) 45%,var(--blue-deep) 100%)}
  .card--front{top:523px;background:var(--paper)}

  .firm-name{font-weight:700;text-transform:uppercase;letter-spacing:.08em;line-height:1.05}
  .card--back .firm-name{position:absolute;left:56px;top:52px;color:#fff;font-size:34px}
  .card--back .firm-name small{display:block;font-size:17px;letter-spacing:.12em;margin-top:4px}

  .corner-tab{position:absolute;left:0;top:0;width:34px;height:34px;background:var(--tab)}
  .card--front .brand{position:absolute;left:60px;top:46px;display:flex;align-items:center;gap:14px}
  .brand-mark{width:34px;height:34px;background:var(--blue)}
  .card--front .firm-name{color:var(--blue);font-size:28px}
  .card--front .firm-name small{display:block;font-size:14px;letter-spacing:.12em;margin-top:3px}

  .side-band{position:absolute;left:60px;top:112px;width:30px;height:220px;background:linear-gradient(180deg,var(--blue) 0%,var(--blue-light) 100%)}
  .contact{position:absolute;left:112px;top:118px;list-style:none;color:var(--ink);font-size:16px;line-height:1.5}
  .contact li{display:flex;align-items:center;gap:8px}
  .contact .spacer{height:10px}
  .contact svg{width:13px;height:13px;fill:var(--blue);flex:none}
  .contact .lbl{color:var(--blue);font-weight:700;width:13px;font-size:13px}

  .person{position:absolute;right:56px;bottom:46px;text-align:right}
  .person-name{color:var(--blue);font-size:26px;font-weight:400}
  .person-title{color:var(--muted);font-size:17px;margin-top:2px}
</style>
</head>
<body>

<section class="card card--back" aria-label="Business card, back">
  <div class="firm-name">Whitfield<small>&amp; Partners CPAs PSC</small></div>
</section>

<section class="card card--front" aria-label="Business card, front">
  <div class="corner-tab"></div>
  <div class="brand">
    <span class="brand-mark"></span>
    <div class="firm-name">Whitfield<small>&amp; Partners CPAs PSC</small></div>
  </div>
  <div class="side-band"></div>
  <ul class="contact">
    <li>4815 Tillamore Ave.</li>
    <li>Suite 1</li>
    <li>Marlow Falls, OR 97019</li>
    <li class="spacer"></li>
    <li><span class="lbl">P</span>541-555-0148</li>
    <li><span class="lbl">F</span>541-555-0149</li>
    <li><svg viewBox="0 0 16 16"><rect x="1" y="3" width="14" height="10" rx="1"/></svg>mdowse@wpfcpa.net</li>
    <li><svg viewBox="0 0 16 16"><circle cx="8" cy="8" r="7"/></svg>www.wpfcpa.net</li>
  </ul>
  <div class="person">
    <div class="person-name">Martin L. Dowse, CPA</div>
    <div class="person-title">Shareholder</div>
  </div>
</section>

</body>
</html>
```